Making our lobbying activities and sports better visible for members and partners.

We are the Velden Assocation of Leisure Gear Merchant and and Trade. We are doing lobbying and having several special groupings and services. With a better power point we want to show better to the board, the members and partner what we are doing.

```html
<!DOCTYPE html>
<html lang="en">
<head>
<meta charset="utf-8">
<title>Velden Assocation of Leisure Gear Merchant and and Trade – Slide Deck Overview</title>
<link href="https://fonts.googleapis.com/css2?family=Anton&family=Open+Sans:wght@400;600;700&display=swap" rel="stylesheet">
<style>
:root{
  --canvas:#dedede;
  --blue:#0aa0e6;
  --blue-mid:#0a86c8;
  --blue-deep:#0b4f7a;
  --navy:#132a3e;
  --ice:#e6f4fb;
  --ink:#111418;
  --grey:#6b7077;
  --light:#eef0f2;
  --purple:#7a2ff0;
  --yellow:#f5c518;
  --orange:#f39217;
  --red:#e5262e;
  --teal:#2fc3c6;
}
*{box-sizing:border-box;margin:0;padding:0}
html,body{width:1200px;height:1200px;overflow:hidden;background:var(--canvas)}
body{position:relative;font-family:"Open Sans",Arial,sans-serif;color:var(--ink)}
.slide{position:absolute;width:249px;height:140px;background:#fff;overflow:hidden}
.abs{position:absolute}
.display{font-family:"Anton",Impact,sans-serif;line-height:1;letter-spacing:.2px}
.blue{color:var(--blue)}
.ink{color:var(--ink)}
.white{color:#fff}
.tiny{font-size:3.4px;line-height:1.4;color:var(--grey)}
.tiny.w{color:#e8f6ff}
.label{font-size:4px;font-weight:600;color:var(--ink)}
.dots{position:absolute;top:8px;left:9px;display:flex;gap:2px}
.dots i{width:3px;height:3px;border-radius:50%;border:1px solid var(--purple)}
.brand{position:absolute;top:9px;right:10px;font-family:"Anton",Impact,sans-serif;font-size:9px;color:var(--ink);letter-spacing:.4px}
.brand.light{color:#fff}
.page{position:absolute;right:7px;bottom:6px;width:6px;height:6px;border-radius:50%;background:var(--purple)}
.photo{position:absolute}
svg{position:absolute;left:0;top:0;overflow:visible}
.swot-letter{position:absolute;font-family:"Anton",Impact,sans-serif;font-size:108px;line-height:1;background:linear-gradient(180deg,var(--navy) 0%,var(--blue-mid) 55%,var(--blue) 100%);-webkit-background-clip:text;background-clip:text;color:transparent}
.kicker{font-size:3px;letter-spacing:.8px;color:var(--grey)}
.btn{display:inline-block;font-size:2.6px;padding:1px 4px;margin-right:3px;border:.5px solid var(--purple);color:var(--purple)}
.btn.fill{background:var(--purple);color:#fff}
.card{position:absolute;background:#fff;box-shadow:0 2px 6px rgba(0,0,0,.12)}
</style>
</head>
<body>

<!-- Title slide -->
<section class="slide" style="left:88px;top:53px;width:509px;height:286px">
  <div class="photo" role="img" aria-label="Physiotherapist guiding an athlete through a stretch in a gym" style="left:0;top:0;width:200px;height:286px;background:linear-gradient(160deg,#d9dde0,#9fb4c2 45%,#5a7d95)"></div>
  <div class="photo" role="img" aria-label="Smiling shopper with sports bag in a clothing store" style="left:340px;top:0;width:169px;height:286px;background:linear-gradient(200deg,#c8c2b8,#8d8278 50%,#3e3a38)"></div>
  <svg width="509" height="286" viewBox="0 0 509 286">
    <defs><linearGradient id="titleBand" x1="0" y1="0" x2="0" y2="1"><stop offset="0" stop-color="#0aa8ef"/><stop offset="1" stop-color="#0b5d92"/></linearGradient></defs>
    <polygon points="72,0 96,0 168,286 156,286" fill="#0aa0e6"/>
    <polygon points="424,0 438,0 362,286 352,286" fill="#0aa0e6"/>
    <polygon points="83,0 427,0 359,286 154,286" fill="url(#titleBand)"/>
  </svg>
  <div class="abs display white" style="left:0;width:509px;top:42px;text-align:center;font-size:26px;letter-spacing:1.5px">VALM</div>
  <div class="abs display white" style="left:0;width:509px;top:108px;text-align:center;font-size:22px;letter-spacing:1px">Velden Assocation</div>
  <div class="abs display white" style="left:0;width:509px;top:136px;text-align:center;font-size:13px;letter-spacing:1px">of Leisure Gear Merchant</div>
  <div class="abs display white" style="left:0;width:509px;top:155px;text-align:center;font-size:13px;letter-spacing:1px">and and Trade</div>
  <div class="abs display white" style="left:195px;top:190px;width:120px;height:27px;background:var(--blue);text-align:center;line-height:27px;font-size:11px;letter-spacing:2px">LET'S BEGIN</div>
</section>

<!-- Welcome -->
<section class="slide" style="left:607px;top:53px;width:248px;height:138px">
  <div class="photo" role="img" aria-label="Balls and sports gear laid out on green grass" style="inset:0;background:radial-gradient(circle at 50% 55%,#4f9a34,#2f6f22 60%,#1f4a18)"></div>
  <div class="abs" style="left:10px;top:8px;width:228px;height:122px;border:.7px solid rgba(255,255,255,.8)"></div>
  <div class="abs display white" style="left:0;width:248px;top:57px;text-align:center;font-size:17px;letter-spacing:1px">WELCOME</div>
  <svg width="248" height="138"><polygon points="248,100 248,138 205,138" fill="var(--blue)"/></svg>
</section>

<!-- Introduction -->
<section class="slide" style="left:863px;top:53px;height:138px">
  <div class="dots"><i></i><i></i><i></i></div>
  <div class="brand">VALM</div>
  <div class="abs display blue" style="left:20px;top:18px;font-size:14px">INTRODUCTION</div>
  <div class="abs" style="left:18px;top:42px;width:212px;height:74px;background:var(--ice);padding:9px 12px">
    <p class="tiny">We bring members and partners together to shape a fair, strong market for leisure gear.</p>
    <p class="tiny" style="margin:6px 0 6px 10px">“Our work gives the trade one clear voice.”</p>
    <p class="tiny">Each group and service is shown here so the board can follow our progress.</p>
  </div>
  <div class="page"></div>
</section>

<!-- About us -->
<section class="slide" style="left:607px;top:199px;width:248px">
  <div class="dots"><i></i><i></i><i></i></div>
  <div class="brand">VALM</div>
  <svg width="248" height="140"><polygon points="138,0 160,0 218,66 196,66" fill="var(--blue-mid)"/><polygon points="168,0 200,0 248,50 248,80" fill="var(--blue)"/></svg>
  <div class="abs display blue" style="left:36px;top:24px;font-size:16px">ABOUT US</div>
  <div class="abs" style="left:36px;top:70px;width:50px;height:6px;background:var(--blue-deep);font-size:3px;color:#cfe;line-height:6px;padding-left:22px">VALM</div>
  <div class="abs" style="left:97px;top:69px;width:105px">
    <p class="tiny">We speak for our members in politics and the market, and we help them grow with practical services.</p>
    <p class="tiny" style="margin-top:8px">“One voice for the leisure trade.”</p>
  </div>
  <div class="page"></div>
</section>

<!-- Quick facts -->
<section class="slide" style="left:863px;top:199px">
  <div class="brand">VALM</div>
  <div class="photo" role="img" aria-label="Shoppers carrying bags in a sports store" style="left:0;top:0;width:130px;height:45px;clip-path:polygon(0 0,100% 0,100% 100%,20% 100%,0 60%);background:linear-gradient(90deg,#6d6a7a,#b9a98a,#d4b24a)"></div>
  <svg width="249" height="140"><polygon points="112,0 122,0 130,45 120,45" fill="#fff"/><polygon points="118,0 128,0 150,28 140,28" fill="var(--blue)"/><line x1="6" y1="95" x2="50" y2="140" stroke="var(--blue)" stroke-width=".8"/></svg>
  <div class="photo" role="img" aria-label="Athletes stretching on a gym floor" style="left:95px;top:101px;width:154px;height:39px;clip-path:polygon(10% 0,100% 0,100% 100%,40% 100%);background:linear-gradient(90deg,#1d2a3a,#3f6b3a,#c9d84a)"></div>
  <div class="abs display ink" style="left:25px;top:52px;font-size:15px">2023</div>
  <div class="abs display blue" style="left:25px;top:69px;font-size:14px">QUICK FACTS</div>
  <svg width="249" height="140">
    <circle cx="146" cy="69" r="13" fill="none" stroke="#222" stroke-width="1.6"/>
    <circle cx="194" cy="69" r="13" fill="none" stroke="var(--blue)" stroke-width="1.6"/>
  </svg>
  <div class="abs display ink" style="left:133px;top:64px;width:26px;text-align:center;font-size:8px">70K</div>
  <div class="abs display blue" style="left:181px;top:64px;width:26px;text-align:center;font-size:8px">200K</div>
  <div class="abs tiny" style="left:130px;top:87px;width:32px;text-align:center">SOME CONTENTS</div>
  <div class="abs tiny" style="left:178px;top:87px;width:32px;text-align:center">SOME CONTENTS</div>
  <div class="page"></div>
</section>

<!-- Our service -->
<section class="slide" style="left:88px;top:353px">
  <div class="photo" role="img" aria-label="Faded sports equipment in soft teal tones" style="inset:0;background:linear-gradient(120deg,#9be3e6,#bfe6f0 50%,#dfe9f6)"></div>
  <svg width="249" height="140"><polygon points="150,15 245,15 175,125 62,125" fill="var(--blue-mid)"/><polygon points="222,62 232,62 200,106 188,106" fill="var(--blue)"/></svg>
  <div class="dots"><i></i><i></i><i></i></div>
  <div class="abs display" style="left:20px;top:18px;font-size:7px;color:var(--navy)">VALM</div>
  <div class="abs display ink" style="left:18px;top:43px;font-size:12px">Our</div>
  <div class="abs display ink" style="left:18px;top:55px;font-size:20px">service</div>
  <div class="abs" style="left:18px;top:80px;width:55px"><p class="tiny" style="color:#334">LOREM IPSUM DOLOR</p><p class="tiny" style="color:#445">We support members with advice, data and events all year long.</p></div>
  <div class="abs" style="left:140px;top:28px;width:60px"><p class="tiny w">Lobbying for fair rules in the leisure gear trade.</p></div>
  <div class="abs" style="left:124px;top:50px;width:60px"><p class="tiny w">Market data and trend reports for every member.</p></div>
  <div class="abs" style="left:108px;top:72px;width:60px"><p class="tiny w">Legal and business advice from our experts.</p></div>
  <div class="abs" style="left:92px;top:94px;width:60px"><p class="tiny w">Shared purchasing and cost savings.</p></div>
  <svg width="249" height="140" fill="none" stroke="#fff" stroke-width=".6">
    <circle cx="132" cy="31" r="3"/><circle cx="116" cy="53" r="3"/><circle cx="100" cy="75" r="3"/><circle cx="84" cy="97" r="3"/>
  </svg>
  <div class="page"></div>
</section>

<!-- In the spirit of sports -->
<section class="slide" style="left:347px;top:353px;width:250px">
  <div class="dots"><i></i><i></i><i></i></div>
  <div class="abs display white" style="right:8px;top:8px;width:30px;height:18px;background:var(--navy);font-size:7px;text-align:center;line-height:18px">VALM</div>
  <div class="photo" role="img" aria-label="Physiotherapist helping an athlete stretch" style="left:0;top:28px;width:150px;height:100px;clip-path:polygon(0 0,75% 0,100% 25%,55% 100%,0 100%);background:linear-gradient(150deg,#d7dde1,#8aa9bd 50%,#45708c)"></div>
  <svg width="250" height="140"><polygon points="120,0 150,0 170,10 135,28" fill="var(--light)"/></svg>
  <div class="abs display ink" style="left:155px;top:51px;font-size:12px">in the spirit of</div>
  <div class="abs display blue" style="left:155px;top:64px;font-size:20px">Sports</div>
  <div class="abs" style="left:155px;top:90px;width:82px"><p class="tiny">LOREM IPSUM DOLOR</p><p class="tiny">Sport brings people together, and our trade keeps them moving with good gear.</p></div>
  <div class="page"></div>
</section>

<!-- And retail -->
<section class="slide" style="left:607px;top:353px;width:248px">
  <div class="dots"><i></i><i></i><i></i></div>
  <div class="brand">VALM</div>
  <div class="abs display ink" style="left:0;width:248px;top:14px;text-align:center;font-size:12px">and</div>
  <div class="abs display blue" style="left:0;width:248px;top:25px;text-align:center;font-size:20px">retail</div>
  <div class="abs tiny" style="left:68px;top:53px;width:112px;text-align:center">Retail is the heart of our association and the link to every customer.</div>
  <svg width="248" height="140">
    <polygon points="28,72 100,72 84,117 12,117" fill="var(--light)"/>
    <polygon points="95,72 170,72 150,117 75,117" fill="var(--blue)"/>
    <polygon points="162,72 235,72 218,117 145,117" fill="var(--light)"/>
    <circle cx="73" cy="82" r="3" fill="none" stroke="var(--teal)" stroke-width=".7"/>
    <path d="M200 84 l8 -4 l2 2 l-8 4 z" fill="none" stroke="var(--red)" stroke-width=".6"/>
  </svg>
  <div class="abs" style="left:30px;top:94px;width:50px;text-align:center"><p class="label" style="font-size:3.4px">Lorem ipsum</p><p class="tiny">Store network and local shops.</p></div>
  <div class="abs" style="left:100px;top:94px;width:50px;text-align:center"><p class="label" style="font-size:3.4px;color:#fff">Lorem ipsum</p><p class="tiny w">Online and mixed channels.</p></div>
  <div class="abs" style="left:165px;top:94px;width:50px;text-align:center"><p class="label" style="font-size:3.4px">Lorem ipsum</p><p class="tiny">Sports shoes and apparel.</p></div>
  <div class="page"></div>
</section>

<!-- High quality goods -->
<section class="slide" style="left:863px;top:353px">
  <div class="dots"><i></i><i></i><i></i></div>
  <div class="brand">VALM</div>
  <div class="abs display blue" style="left:0;width:249px;top:17px;text-align:center;font-size:14px">High Quality Goods</div>
  <div class="abs tiny" style="left:80px;top:37px;width:90px;text-align:center">Members sell tested products that meet high standards.</div>
  <div class="photo" role="img" aria-label="Collage of shoppers and athletes in a zigzag frame" style="left:18px;top:51px;width:213px;height:75px;clip-path:polygon(0 0,22% 0,35% 70%,50% 20%,65% 70%,78% 0,100% 0,68% 100%,50% 55%,32% 100%);background:linear-gradient(90deg,#3f4f6a,#8a6e4c,#4d7a3c,#c9a33a,#2d4563)"></div>
  <div class="page"></div>
</section>

<!-- Our strategy -->
<section class="slide" style="left:88px;top:505px">
  <svg width="249" height="140"><polygon points="115,0 249,0 249,60 170,140 20,140" fill="var(--ice)"/></svg>
  <div class="dots"><i></i><i></i><i></i></div>
  <div class="brand">VALM</div>
  <div class="abs display" style="left:26px;top:37px;font-size:15px"><span class="ink">Our </span><span class="blue">Strategy</span></div>
  <div class="abs tiny" style="left:163px;top:38px;width:60px">Three steps guide our work this year.</div>
  <svg width="249" height="140">
    <polygon points="22,60 98,60 84,104 10,104" fill="var(--ink)"/>
    <polygon points="100,60 172,60 158,104 86,104" fill="#fff" stroke="#ddd" stroke-width=".4"/>
    <polygon points="174,60 246,60 232,104 160,104" fill="var(--blue)"/>
    <rect x="38" y="104" width="26" height="5" fill="var(--blue-deep)"/>
    <rect x="110" y="104" width="26" height="5" fill="var(--blue-deep)"/>
    <rect x="182" y="104" width="26" height="5" fill="var(--blue-deep)"/>
  </svg>
  <div class="abs" style="left:22px;top:67px;width:60px;text-align:center"><p class="label" style="color:#ccc;font-weight:400">Your Text in Here</p><p class="tiny w" style="margin-top:3px">Build a strong voice in politics for our whole trade.</p></div>
  <div class="abs" style="left:98px;top:67px;width:60px;text-align:center"><p class="label" style="font-weight:400;color:#555">Your Text in Here</p><p class="tiny" style="margin-top:3px">Grow services that save members time and money.</p></div>
  <div class="abs" style="left:170px;top:67px;width:60px;text-align:center"><p class="label" style="font-weight:400;color:#dff">Your Text in Here</p><p class="tiny w" style="margin-top:3px">Share results clearly with the board and partners.</p></div>
  <div class="abs white" style="left:38px;top:104px;width:26px;text-align:center;font-size:3.5px;font-weight:700">01</div>
  <div class="abs white" style="left:110px;top:104px;width:26px;text-align:center;font-size:3.5px;font-weight:700">02</div>
  <div class="abs white" style="left:182px;top:104px;width:26px;text-align:center;font-size:3.5px;font-weight:700">03</div>
  <div class="page"></div>
</section>

<!-- Gallery slides -->
<section class="slide" style="left:347px;top:505px;width:250px">
  <div class="dots"><i></i><i></i><i></i></div>
  <svg width="250" height="140"><line x1="45" y1="0" x2="82" y2="28" stroke="var(--blue)" stroke-width=".7"/><polygon points="0,100 8,92 48,140 40,140" fill="var(--blue)"/><polygon points="0,0 4,0 4,60 0,60" fill="var(--purple)"/></svg>
  <div class="abs display blue" style="left:28px;top:37px;font-size:17px;line-height:1.05">GALLERY<br>SLIDES</div>
  <div class="abs" style="left:28px;top:76px;width:78px;font-size:4px;line-height:1.4;color:#444">Moments from our events, fairs and member days, shown together in one place.</div>
  <div class="photo" role="img" aria-label="Shoppers in a sports store" style="left:110px;top:0;width:70px;height:52px;background:linear-gradient(135deg,#5b6b7d,#9c8a63)"></div>
  <div class="photo" role="img" aria-label="Sports balls on grass" style="left:180px;top:0;width:35px;height:34px;background:linear-gradient(135deg,#3f7a2b,#2b5320)"></div>
  <div class="photo" role="img" aria-label="Athletes stretching" style="left:110px;top:54px;width:35px;height:52px;background:linear-gradient(135deg,#465f7a,#b7c444)"></div>
  <div class="photo" role="img" aria-label="Customers choosing clothing" style="left:215px;top:70px;width:35px;height:38px;background:linear-gradient(135deg,#8b7a6a,#c9b24c)"></div>
  <div class="photo" role="img" aria-label="Gym training session" style="left:180px;top:108px;width:70px;height:32px;background:linear-gradient(135deg,#9aaab8,#41607a)"></div>
  <div class="abs display ink" style="left:185px;top:44px;font-size:9px">VALM</div>
  <div class="page"></div>
</section>

<!-- Break section -->
<section class="slide" style="left:607px;top:505px;width:250px">
  <div class="photo" role="img" aria-label="Athlete training in a gym in teal tones" style="left:70px;top:8px;width:112px;height:132px;background:linear-gradient(160deg,#a5e6ea,#55c4d2 60%,#2fa6c0)"></div>
  <svg width="250" height="140">
    <polygon points="175,0 250,0 250,20 195,90 160,90" fill="var(--blue)"/>
    <polygon points="40,140 70,110 150,110 120,140" fill="var(--blue-mid)" opacity=".85"/>
  </svg>
  <div class="brand" style="left:22px;right:auto;top:7px">VALM</div>
  <div class="abs display ink" style="left:20px;top:26px;font-size:24px">BREAK</div>
  <div class="abs" style="left:22px;top:54px;width:50px;height:5px;background:var(--blue-deep);font-size:3px;color:#cfe;line-height:5px;text-align:center">30 MINUTES BREAK</div>
  <div class="abs display ink" style="left:125px;top:64px;font-size:24px">SECTION</div>
</section>

<!-- Our short story -->
<section class="slide" style="left:863px;top:505px">
  <div class="dots"><i></i><i></i><i></i></div>
  <div class="brand">VALM</div>
  <div class="abs display ink" style="left:0;width:249px;top:12px;text-align:center;font-size:12px">Our short</div>
  <div class="abs display blue" style="left:0;width:249px;top:26px;text-align:center;font-size:19px">Story</div>
  <div class="abs" style="left:0;top:96px;width:249px;height:2px;background:var(--light)"></div>
  <svg width="249" height="140">
    <polygon points="34,78 40,70 46,78 46,96 34,96" fill="var(--ink)"/>
    <polygon points="67,83 79,83 79,101 73,107 67,101" fill="var(--teal)"/>
    <polygon points="101,72 107,66 113,72 113,96 101,96" fill="var(--yellow)"/>
    <polygon points="135,83 147,83 147,101 141,107 135,101" fill="var(--orange)"/>
    <polygon points="168,72 174,66 180,72 180,96 168,96" fill="var(--red)"/>
    <polygon points="202,83 214,83 214,101 208,107 202,101" fill="var(--blue)"/>
  </svg>
  <div class="abs white" style="left:34px;top:88px;width:12px;text-align:center;font-size:3.6px;font-weight:700">2018</div>
  <div class="abs white" style="left:67px;top:85px;width:12px;text-align:center;font-size:3.6px;font-weight:700">2019</div>
  <div class="abs white" style="left:101px;top:88px;width:12px;text-align:center;font-size:3.6px;font-weight:700">2020</div>
  <div class="abs white" style="left:135px;top:85px;width:12px;text-align:center;font-size:3.6px;font-weight:700">2021</div>
  <div class="abs white" style="left:168px;top:88px;width:12px;text-align:center;font-size:3.6px;font-weight:700">2022</div>
  <div class="abs white" style="left:202px;top:85px;width:12px;text-align:center;font-size:3.6px;font-weight:700">2023</div>
  <div class="abs tiny" style="left:55px;top:61px;width:36px;text-align:center">LOREM IPSUM<br>New board formed.</div>
  <div class="abs tiny" style="left:123px;top:61px;width:36px;text-align:center">LOREM IPSUM<br>First member fair.</div>
  <div class="abs tiny" style="left:190px;top:61px;width:36px;text-align:center">LOREM IPSUM<br>New services.</div>
  <div class="abs tiny" style="left:22px;top:112px;width:36px;text-align:center">LOREM IPSUM<br>Association founded.</div>
  <div class="abs tiny" style="left:89px;top:112px;width:36px;text-align:center">LOREM IPSUM<br>Online events.</div>
  <div class="abs tiny" style="left:156px;top:112px;width:36px;text-align:center">LOREM IPSUM<br>Trade law win.</div>
  <div class="page"></div>
</section>

<!-- Report -->
<section class="slide" style="left:88px;top:656px">
  <svg width="249" height="140"><polygon points="210,35 249,35 249,60 225,60" fill="var(--blue-mid)"/><polygon points="100,140 160,110 249,110 249,140" fill="var(--blue)"/><polygon points="180,140 200,120 220,120 200,140" fill="#fff"/></svg>
  <div class="dots"><i></i><i></i><i></i></div>
  <div class="brand">VALM</div>
  <div class="abs display blue" style="left:23px;top:16px;font-size:15px">VALM Report</div>
  <div class="card" style="left:22px;top:50px;width:70px;height:35px;padding:5px 7px"><p class="display ink" style="font-size:10px"><span class="blue">↑</span> 40%</p><p class="tiny" style="margin-top:3px">Members report growth in sales this year.</p></div>
  <div class="card" style="left:22px;top:92px;width:70px;height:35px;padding:5px 7px"><p class="display ink" style="font-size:10px"><span class="blue">↓</span> 15%</p><p class="tiny" style="margin-top:3px">Lower costs through shared buying.</p></div>
  <div class="card" style="left:115px;top:50px;width:110px;height:78px"></div>
  <svg width="249" height="140" fill="none" stroke-width=".7">
    <line x1="125" y1="56" x2="125" y2="116" stroke="#bbb"/><line x1="125" y1="116" x2="220" y2="116" stroke="#bbb"/>
    <polyline points="128,110 138,90 146,100 156,78 166,96 176,82 186,92 198,74 210,84 218,80" stroke="var(--yellow)"/>
    <polyline points="128,112 140,98 150,106 160,90 170,102 182,86 192,96 204,84 214,90" stroke="var(--blue)"/>
    <circle cx="182" cy="86" r="1.2" fill="var(--blue)"/>
  </svg>
  <div class="abs tiny" style="left:130px;top:118px">LOW VALUE</div>
  <div class="abs tiny" style="left:190px;top:118px">HIGH VALUE</div>
  <div class="page"></div>
</section>

<!-- Investment -->
<section class="slide" style="left:350px;top:656px;width:247px">
  <svg width="247" height="140"><polygon points="155,10 175,10 120,140 100,140" fill="var(--blue)"/><polygon points="200,0 247,0 247,50 170,140 140,140" fill="var(--light)"/><polygon points="225,100 235,100 205,140 195,140" fill="var(--ink)"/></svg>
  <div class="dots"><i></i><i></i><i></i></div>
  <div class="brand">VALM</div>
  <div class="abs display blue" style="left:22px;top:34px;font-size:19px">investment</div>
  <div class="abs" style="left:22px;top:60px;width:80px"><p class="tiny">LOREM IPSUM DOLOR</p><p class="tiny">We invest in training, research and events that help our members stay strong.</p></div>
  <div class="abs display ink" style="left:22px;top:92px;font-size:7px">45,045</div>
  <div class="abs tiny" style="left:22px;top:102px;width:60px">Visitors at our trade days.</div>
  <div class="card" style="left:125px;top:35px;width:95px;height:80px"></div>
  <div class="abs" style="left:122px;top:33px;width:55px;height:18px;background:var(--navy);padding:3px 4px"><p class="white" style="font-size:4.5px;font-weight:700">$347.00</p><p class="tiny w">Yearly fee per member</p></div>
  <svg width="247" height="140"><polygon points="130,80 145,72 155,76 168,60 176,48 184,62 192,70 200,66 214,80" fill="var(--blue-deep)"/><polyline points="150,74 168,58 176,44 184,58 196,64 212,72" fill="none" stroke="var(--orange)" stroke-width=".7"/></svg>
  <div class="abs blue" style="left:130px;top:84px;font-size:7px">3420+</div>
  <div class="abs tiny" style="left:130px;top:95px;width:80px">Hours of training given to member staff.</div>
  <div class="page"></div>
</section>

<!-- SWOT: Strength -->
<section class="slide" style="left:607px;top:658px;width:245px;height:138px">
  <div class="brand">VALM</div>
  <div class="swot-letter" style="left:20px;top:6px">S</div>
  <div class="abs kicker" style="left:98px;top:35px">SWOT ANALYSIS</div>
  <div class="abs display blue" style="left:98px;top:42px;font-size:17px">Strength</div>
  <div class="abs" style="left:98px;top:69px;display:flex;align-items:center;gap:3px"><svg style="position:static" width="7" height="8"><path d="M1 0h5v3a2.5 2.5 0 0 1-5 0z M3 5.5v1.5 M1.5 7.5h4" fill="var(--orange)" stroke="var(--ink)" stroke-width=".5"/></svg><span class="display ink" style="font-size:9px">2022</span><span class="tiny" style="font-size:3.6px">Throphy<br>Text in Here</span></div>
  <div class="abs tiny" style="left:98px;top:84px;width:95px">A strong network of shops and brands gives us weight in every debate.</div>
  <div class="abs" style="left:98px;top:97px"><span class="btn fill">Read more</span><span class="btn">Read more</span></div>
  <div class="page"></div>
</section>

<!-- SWOT: Weaknesses -->
<section class="slide" style="left:865px;top:656px;width:247px">
  <div class="brand">VALM</div>
  <div class="swot-letter" style="left:3px;top:6px;font-size:104px">W</div>
  <div class="abs kicker" style="left:99px;top:35px">SWOT ANALYSIS</div>
  <div class="abs display blue" style="left:99px;top:42px;font-size:17px">Weaknesses</div>
  <div class="abs tiny" style="left:99px;top:67px;width:80px">Small shops have little time to take part in our working groups.</div>
  <div class="abs" style="left:99px;top:87px;display:flex;align-items:center;gap:4px"><span class="display ink" style="font-size:12px">35</span><span class="tiny" style="font-size:3.6px">Learning<br>Your Text in Here</span></div>
  <div class="page"></div>
</section>

<!-- SWOT: Opportunities -->
<section class="slide" style="left:88px;top:807px;width:248px">
  <div class="dots"><i></i><i></i><i></i></div>
  <div class="brand">VALM</div>
  <div class="swot-letter" style="left:22px;top:6px">O</div>
  <div class="abs kicker" style="left:99px;top:35px">SWOT ANALYSIS</div>
  <div class="abs display blue" style="left:99px;top:42px;font-size:17px">Opportunitie<br>s</div>
  <div class="abs" style="left:99px;top:70px;display:flex;align-items:center;gap:3px"><span class="display ink" style="font-size:9px">2022</span><span class="tiny" style="font-size:3.6px">Throphy<br>Text in Here</span></div>
  <div class="abs tiny" style="left:99px;top:84px;width:95px">New outdoor trends open doors for our members and partners.</div>
  <div class="abs" style="left:99px;top:97px"><span class="btn fill">Read more</span><span class="btn">Read more</span></div>
  <div class="page"></div>
</section>

<!-- SWOT: Threats -->
<section class="slide" style="left:347px;top:807px;width:248px">
  <div class="dots"><i></i><i></i><i></i></div>
  <div class="brand">VALM</div>
  <div class="swot-letter" style="left:22px;top:6px">T</div>
  <div class="abs kicker" style="left:99px;top:35px">SWOT ANALYSIS</div>
  <div class="abs display blue" style="left:99px;top:42px;font-size:17px">Threats</div>
  <div class="abs tiny" style="left:99px;top:67px;width:85px">Large online platforms put pressure on prices and local stores.</div>
  <div class="abs" style="left:99px;top:87px;display:flex;align-items:center;gap:4px"><span class="display ink" style="font-size:12px">35</span><span class="tiny" style="font-size:3.6px">Learning<br>Your Text in Here</span></div>
  <div class="page"></div>
</section>

<!-- Social media -->
<section class="slide" style="left:607px;top:809px;width:250px;height:140px">
  <div class="photo" role="img" aria-label="Shoppers walking in a mall in teal tones" style="left:0;top:0;width:250px;height:75px;background:linear-gradient(90deg,#7fd9dc,#b8eaea 40%,#5fc9d4)"></div>
  <div class="brand">VALM</div>
  <div class="abs display ink" style="left:0;width:250px;top:16px;text-align:center;font-size:14px">Social Media</div>
  <svg width="250" height="140">
    <polyline points="42,64 82,57 122,74 162,57 202,72" fill="none" stroke="var(--navy)" stroke-width="1.6"/>
    <g fill="#fff" stroke="#ddd" stroke-width=".4"><rect x="34" y="56" width="16" height="16"/><rect x="74" y="49" width="16" height="16"/><rect x="114" y="66" width="16" height="16"/><rect x="154" y="49" width="16" height="16"/><rect x="194" y="64" width="16" height="16"/></g>
    <circle cx="42" cy="64" r="4" fill="var(--red)"/><circle cx="82" cy="57" r="4" fill="#22a84a"/><circle cx="122" cy="74" r="4" fill="var(--blue)"/><circle cx="162" cy="57" r="4" fill="var(--blue-deep)"/><circle cx="202" cy="72" r="4" fill="#1f5fc4"/>
  </svg>
  <div class="abs" style="left:22px;top:98px;width:40px;text-align:center"><p class="label" style="font-weight:400">Text in Here</p><p class="tiny">Short video news.</p></div>
  <div class="abs" style="left:62px;top:82px;width:40px;text-align:center"><p class="label" style="font-weight:400">Text in Here</p><p class="tiny">Member chat group.</p></div>
  <div class="abs" style="left:102px;top:98px;width:40px;text-align:center"><p class="label" style="font-weight:400">Text in Here</p><p class="tiny">Quick updates.</p></div>
  <div class="abs" style="left:142px;top:82px;width:40px;text-align:center"><p class="label" style="font-weight:400">Text in Here</p><p class="tiny">Partner network.</p></div>
  <div class="abs" style="left:182px;top:98px;width:40px;text-align:center"><p class="label" style="font-weight:400">Text in Here</p><p class="tiny">Events and photos.</p></div>
  <div class="page"></div>
</section>

<!-- World map -->
<section class="slide" style="left:865px;top:807px;width:247px">
  <div class="dots"><i></i><i></i><i></i></div>
  <div class="brand">VALM</div>
  <div class="abs display blue" style="left:0;width:247px;top:18px;text-align:center;font-size:16px">World map</div>
  <div class="photo" role="img" aria-label="World map with member regions highlighted" style="left:38px;top:48px;width:170px;height:80px;border-radius:40%;background:radial-gradient(ellipse at center,#c9cbce,#e4e5e7 70%,#fff)"></div>
  <div class="abs" style="left:28px;top:96px"><p class="display ink" style="font-size:9px">80%</p><p class="tiny" style="width:38px">Members in the home region.</p></div>
  <div class="abs" style="left:200px;top:96px"><p class="display blue" style="font-size:9px">53%</p><p class="tiny" style="width:36px">Export to partner countries.</p></div>
  <div class="page"></div>
</section>

<!-- Options -->
<section class="slide" style="left:88px;top:958px">
  <div class="dots"><i></i><i></i><i></i></div>
  <div class="brand">VALM</div>
  <svg width="249" height="140" fill="none" stroke-width="11">
    <path d="M33 72 A28 28 0 0 1 55 45" stroke="var(--ink)"/>
    <path d="M62 43 A28 28 0 0 1 89 60" stroke="var(--blue)"/>
    <path d="M92 68 A28 28 0 0 1 78 96" stroke="var(--yellow)"/>
    <path d="M70 100 A28 28 0 0 1 38 90" stroke="var(--orange)"/>
  </svg>
  <div class="abs white" style="left:60px;top:44px;font-size:3.6px;transform:rotate(15deg)">OPTION 02</div>
  <div class="abs white" style="left:46px;top:104px;font-size:3.6px;transform:rotate(15deg)">OPTION 04</div>
  <div class="abs white" style="left:16px;top:66px;font-size:3.6px;transform:rotate(-80deg)">OPTION 01</div>
  <div class="abs" style="left:86px;top:70px;font-size:3.6px;color:#7a5a00;transform:rotate(80deg)">OPTION 03</div>
  <div class="abs display blue" style="left:118px;top:25px;font-size:18px">Options</div>
  <div class="abs" style="left:118px;top:50px;width:110px"><p class="tiny">LOREM IPSUM DOLOR</p><p class="tiny">Members can choose from four service packages that fit their needs.</p></div>
  <svg width="249" height="140"><circle cx="124" cy="82" r="6" fill="var(--ink)"/><circle cx="184" cy="82" r="6" fill="var(--blue)"/><circle cx="124" cy="104" r="6" fill="var(--yellow)"/><circle cx="184" cy="104" r="6" fill="var(--orange)"/></svg>
  <div class="abs tiny" style="left:133px;top:78px;width:44px">LOREM IPSUM<br>Basic membership.</div>
  <div class="abs tiny" style="left:193px;top:78px;width:44px">LOREM IPSUM<br>Advice and data.</div>
  <div class="abs tiny" style="left:133px;top:100px;width:44px">LOREM IPSUM<br>Events and fairs.</div>
  <div class="abs tiny" style="left:193px;top:100px;width:44px">LOREM IPSUM<br>Full partner plan.</div>
  <div class="page"></div>
</section>

<!-- Get in touch -->
<section class="slide" style="left:347px;top:958px;width:250px">
  <div class="photo" role="img" aria-label="Regional road map with office location" style="left:110px;top:10px;width:140px;height:130px;clip-path:polygon(30% 0,100% 0,100% 100%,0 100%,0 40%);background:linear-gradient(150deg,#e6ede0,#cfe0c6 50%,#b9d3b0)"></div>
  <svg width="250" height="140"><polygon points="20,0 110,0 70,40 40,40" fill="var(--light)"/><path d="M215 48 a5 5 0 1 1 10 0 c0 4 -5 9 -5 9 s-5 -5 -5 -9z" fill="var(--teal)"/><circle cx="220" cy="48" r="1.8" fill="#fff"/></svg>
  <div class="dots"><i></i><i></i><i></i></div>
  <div class="brand">VALM</div>
  <div class="abs display ink" style="left:38px;top:30px;font-size:12px">Get in</div>
  <div class="abs display blue" style="left:38px;top:42px;font-size:19px">touch</div>
  <div class="abs" style="left:20px;top:64px;width:128px;height:58px;background:linear-gradient(90deg,var(--blue-deep),var(--blue-mid));padding:6px 12px">
    <p class="white" style="font-size:3.6px">Overview</p>
    <p class="tiny w">Call, write or visit our office. We are glad to help members and partners.</p>
    <p class="white" style="font-size:3.6px;margin-top:9px;border-top:.4px solid rgba(255,255,255,.4);padding-top:3px">Social Media</p>
    <p class="tiny w" style="margin-top:3px">▪ FOLLOW US &nbsp;&nbsp;&nbsp;&nbsp;&nbsp;&nbsp;&nbsp;&nbsp;&nbsp;&nbsp; ▪ NEWS FEED</p>
  </div>
  <div class="abs tiny" style="left:160px;top:72px;color:var(--red)">Velden Region</div>
  <div class="page"></div>
</section>

<!-- Contact us -->
<section class="slide" style="left:607px;top:958px;width:251px">
  <div class="dots"><i></i><i></i><i></i></div>
  <div class="brand">VALM</div>
  <svg width="251" height="140">
    <defs><linearGradient id="contactBand" x1="0" y1="0" x2="1" y2="0"><stop offset="0" stop-color="#071d2e"/><stop offset="1" stop-color="#0a86c8"/></linearGradient></defs>
    <polygon points="45,20 210,20 195,60 30,60" fill="var(--blue)"/>
    <polygon points="40,60 232,60 208,126 20,126" fill="url(#contactBand)"/>
  </svg>
  <div class="abs display white" style="left:0;width:251px;top:50px;text-align:center;font-size:20px">contact us</div>
  <div class="abs" style="left:70px;top:78px;width:130px">
    <p class="white" style="font-size:3.8px">Address</p>
    <p class="tiny w">Seestrasse 12, 9220 Velden – visits by appointment.</p>
  </div>
  <div class="abs tiny w" style="left:72px;top:102px">● mail@valm-trade.org</div>
  <div class="abs tiny w" style="left:130px;top:102px">● www.valm-trade.org</div>
  <div class="abs tiny w" style="left:72px;top:110px">● +43 0000 000 000</div>
  <div class="abs tiny w" style="left:130px;top:110px">● VALM</div>
  <div class="page"></div>
</section>

<!-- Thank you -->
<section class="slide" style="left:865px;top:961px;width:246px;height:138px">
  <div class="abs" style="inset:0;background:linear-gradient(135deg,#0b7fbe,#0a9de2 50%,#0b5f94)"></div>
  <svg width="246" height="138"><polygon points="0,30 40,0 95,0 20,70" fill="#0b4f7a" opacity=".6"/><polygon points="180,138 246,60 246,138" fill="#0aa8ef"/></svg>
  <div class="photo" role="img" aria-label="Two smiling shoppers holding bags in a mall" style="left:95px;top:0;width:90px;height:138px;background:linear-gradient(180deg,#d9d6d2,#9a8a7f 50%,#4c4a55)"></div>
  <div class="abs display white" style="left:0;width:246px;top:44px;text-align:center;font-size:30px;letter-spacing:1px">thank you</div>
</section>

</body>
</html>
```